Plush Dwellings website

full website from start to finish. I would like something like this -
https://www.quarrybendmanors.example/
http://tidalcrestvillas.example/

Target Market(s)

real estate investors

Industry/Entity Type

Real Estate

Number of Pages Required

5+ page

Font styles to use
Sans Serif

Colors

Designer to choose colors to be used in the design.

Requirements
Must have
• translated in English, Spanish and japanese

```html
<!DOCTYPE html>
<html lang="en">
<head>
<meta charset="utf-8">
<title>Plush Dwellings</title>
<link href="https://fonts.googleapis.com/css2?family=Mulish:wght@400;600;700;800&family=Open+Sans:wght@400;600&display=swap" rel="stylesheet">
<style>
:root{
  --red:#d81c32;
  --ink:#222;
  --text:#333;
  --muted:#9a9a9a;
  --grey-band:#f3f3f3;
  --panel:#dcdcdc;
  --dark:#262626;
  --white:#fff;
}
*{margin:0;padding:0;box-sizing:border-box}
html,body{width:1200px;height:2866px;overflow:hidden}
body{position:relative;background:var(--white);font-family:"Open Sans",Arial,sans-serif;color:var(--text)}
.abs{position:absolute}
.heading{font-family:"Mulish",Arial,sans-serif;color:var(--red);font-weight:600;font-size:34px;text-align:center;width:1200px;left:0;letter-spacing:.5px}

/* hero */
.hero-photo{left:0;top:0;width:1200px;height:700px;background:linear-gradient(180deg,#2d6fb8 0%,#6aa6d6 38%,#a8c7d8 55%,#6e9fb8 75%,#2c5f86 100%)}
.hero-house{left:560px;top:60px;width:640px;height:520px;background:linear-gradient(160deg,#cfd3d6 0%,#9ea4a8 45%,#6e6a64 100%)}
.hero-shapes{left:0;top:0}
.header-bar{left:132px;top:10px;width:934px;height:62px;background:var(--white)}
.brand{left:18px;top:10px;font-family:"Mulish",Arial,sans-serif;font-size:34px;color:var(--red);font-weight:400}
.phone{left:562px;top:17px;font-family:"Mulish",Arial,sans-serif;font-size:22px;color:#444;display:flex;align-items:center;gap:8px}
.langs{left:757px;top:23px;font-size:12px;color:#555}
.langs span{margin:0 6px}
.nav{left:132px;top:72px;width:934px;height:39px;background:var(--red);display:flex;justify-content:space-between;align-items:center;padding:0 14px}
.nav a{color:var(--white);text-decoration:none;font-size:12.5px;font-weight:600;text-transform:uppercase}
.hero-kicker{left:132px;top:276px;font-family:"Mulish",Arial,sans-serif;font-size:32px;color:var(--white)}
.hero-title{left:132px;top:316px;font-family:"Mulish",Arial,sans-serif;font-size:37px;font-weight:800;color:var(--white);letter-spacing:.5px}
.btn-dark{left:132px;top:367px;width:105px;height:38px;background:#2c2c2c;color:var(--white);font-size:12px;display:flex;align-items:center;justify-content:center;text-transform:uppercase}
.arrow{top:326px;width:29px;height:29px;background:#222;display:flex;align-items:center;justify-content:center}

/* welcome */
.welcome-title{top:718px}
.welcome-text{left:132px;top:766px;width:936px;text-align:center;font-size:13px;line-height:24px;color:#444}

/* properties */
.grey-band{left:0;top:940px;width:1200px;height:1000px;background:var(--grey-band)}
.props-title{top:1082px}
.card{width:298px;height:302px;background:var(--white)}
.card .photo{width:298px;height:199px}
.card p{position:absolute;left:18px;top:215px;width:262px;font-size:14.5px;line-height:21px;color:#333}
.card .price{position:absolute;left:18px;top:264px;font-size:14.5px;color:var(--red)}
.btn-red{left:548px;top:1802px;width:104px;height:48px;background:var(--red);color:var(--white);font-family:"Mulish",Arial,sans-serif;font-size:14px;font-weight:600;display:flex;align-items:center;justify-content:center}

/* testimonial */
.video-photo{left:0;top:1949px;width:600px;height:369px;background:linear-gradient(180deg,#5d8fd0 0%,#8fb2c9 35%,#b99c72 60%,#9c6a58 85%,#7a5d4e 100%)}
.quote-panel{left:600px;top:1905px;width:600px;height:413px;background:var(--panel)}
.quote-text{left:652px;top:2063px;width:430px;font-family:"Mulish",Arial,sans-serif;font-size:25px;line-height:37px;color:#333}
.quote-name{left:652px;top:2232px;font-family:"Mulish",Arial,sans-serif;font-size:20px;color:var(--red)}

/* contact */
.contact-title{top:2396px}
.contact-line{left:0;width:1200px;text-align:center;font-family:"Mulish",Arial,sans-serif;font-size:19px;color:#222}

/* footer */
.footer{left:0;top:2560px;width:1200px;height:306px}
.social{left:480px;top:2702px;display:flex;gap:17px}
.social span{width:34px;height:34px;background:var(--red);display:block}
.footer-links{left:0;top:2767px;width:1200px;text-align:center;font-size:11.5px;color:#aaa}
.footer-links span{margin:0 7px}
.copyright{left:0;top:2797px;width:1200px;text-align:center;font-size:11.5px;color:#aaa}
</style>
</head>
<body>

<!-- hero -->
<div class="abs hero-photo" role="img" aria-label="Photo of a modern glass villa with an infinity pool facing the sea"></div>
<div class="abs hero-house" role="img" aria-label="Modern two storey villa with glazed walls"></div>
<svg class="abs hero-shapes" width="1200" height="720" viewBox="0 0 1200 720">
  <polygon points="0,652 620,615 0,690" fill="#111"/>
  <polygon points="540,620 1200,537 1200,575" fill="var(--red)"/>
  <polygon points="0,690 1200,572 1200,720 0,720" fill="#fff"/>
</svg>

<div class="abs header-bar">
  <div class="abs brand">Plush Dwellings</div>
  <div class="abs phone">
    <svg width="18" height="18" viewBox="0 0 24 24"><path d="M6.6 10.8a15 15 0 0 0 6.6 6.6l2.2-2.2a1 1 0 0 1 1-.25 11.4 11.4 0 0 0 3.6.57 1 1 0 0 1 1 1V20a1 1 0 0 1-1 1A17 17 0 0 1 3 4a1 1 0 0 1 1-1h3.5a1 1 0 0 1 1 1c0 1.25.2 2.45.57 3.57a1 1 0 0 1-.25 1z" fill="#444"/></svg>
    555 014 2873
  </div>
  <div class="abs langs">English <span>|</span> Español <span>|</span> 日本語</div>
</div>
<nav class="abs nav">
  <a>Our Properties</a><a>Specials</a><a>Gallery</a><a>Testimonials</a><a>About Us</a><a>Contact Us</a><a>Search Properties</a>
</nav>

<div class="abs hero-kicker">Etiam mattis</div>
<div class="abs hero-title">AUGUE VEHICULA</div>
<div class="abs btn-dark">Read More</div>
<div class="abs arrow" style="left:0">
  <svg width="14" height="14" viewBox="0 0 14 14"><path d="M12 7H3M6 3 2 7l4 4" stroke="#fff" stroke-width="2" fill="none"/></svg>
</div>
<div class="abs arrow" style="left:1171px">
  <svg width="14" height="14" viewBox="0 0 14 14"><path d="M2 7h9M8 3l4 4-4 4" stroke="#fff" stroke-width="2" fill="none"/></svg>
</div>

<!-- welcome -->
<h2 class="abs heading welcome-title">WELCOME</h2>
<p class="abs welcome-text">Fusce nec leo ac urna pulvinar auctor. Mauris bibendum fringilla velit. Nulla in lorem at massa pellentesque posuere. Nulla tristique posuere molestie. Aliquam erat volutpat. Etiam quis aliquet risus. Duis ornare erat eget magna dapibus, in accumsan quam pharetra. Nam tempus, quam in bibendum vulputate, sapien dolor viverra nisl, vitae euismod elit turpis et nulla. Aliquam erat volutpat. Pellentesque blandit lacus eget nunc faucibus, et tincidunt eros viverra. Phasellus consequat sagittis nisi suscipit feugiat. Cras eget leo sed nunc hendrerit ultricies eu at nisl.</p>

<!-- properties -->
<div class="abs grey-band"></div>
<svg class="abs" style="left:0;top:940px" width="1200" height="90" viewBox="0 0 1200 90">
  <polygon points="0,0 1200,0 1200,2 0,82" fill="#fff"/>
  <polygon points="0,82 1200,2 1200,55" fill="var(--red)"/>
</svg>
<h2 class="abs heading props-title">PROPERTIES</h2>

<div class="abs card" style="left:132px;top:1139px">
  <div class="photo" role="img" aria-label="Open living room with sea view" style="background:linear-gradient(180deg,#8fc8e8,#e8eef0 60%,#cfd6d8)"></div>
  <p>Sed augue orci, elementum in magna congue tincidunt</p><span class="price">$ 3,000,000</span>
</div>
<div class="abs card" style="left:451px;top:1139px">
  <div class="photo" role="img" aria-label="Glass villa beside a lit pool at dusk" style="background:linear-gradient(160deg,#3b76b8,#8fb8d8 45%,#2a4a66 80%,#1a8ac8)"></div>
  <p>Aliquam consectetur orci molestie dictum molestie.</p><span class="price">$ 3,200,000</span>
</div>
<div class="abs card" style="left:770px;top:1139px">
  <div class="photo" role="img" aria-label="Hillside home with garden lights overlooking a bay at night" style="background:linear-gradient(180deg,#2a4f8c,#4a6aa0 40%,#7a5a4a 70%,#8a5a6a)"></div>
  <p>Vestibulum condimentum, risus ut posuere cursus, velit justo accumsan</p><span class="price">$ 4,000,000</span>
</div>
<div class="abs card" style="left:132px;top:1466px">
  <div class="photo" role="img" aria-label="Beach house with deck and lawn by the ocean" style="background:linear-gradient(180deg,#3a7ac8,#9cc4e4 45%,#c8b89a 70%,#7a8a5a)"></div>
  <p>Pellentesque a imperdiet dolor, et auctor est</p><span class="price">$ 5,100,000</span>
</div>
<div class="abs card" style="left:451px;top:1466px">
  <div class="photo" role="img" aria-label="Family house with warm lit windows at twilight" style="background:linear-gradient(180deg,#1c2f4f,#3a4a5a 45%,#8a6a4a 70%,#3a4a2a)"></div>
  <p>Fusce sollicitudin lorem et luctus volutpat. Proin placerat dapibus</p><span class="price">$ 2,200,000</span>
</div>
<div class="abs card" style="left:770px;top:1466px">
  <div class="photo" role="img" aria-label="Contemporary house with long pool and trees" style="background:linear-gradient(180deg,#e8eef2,#8a8a86 45%,#4a6a88 70%,#5aa8d8)"></div>
  <p>Maecenas vel tortor accumsan quam varius imperdiet</p><span class="price">$ 5,000,000</span>
</div>

<div class="abs btn-red">View All</div>

<!-- testimonial -->
<div class="abs quote-panel"></div>
<div class="abs video-photo" role="img" aria-label="Mediterranean style mansion with palm trees and a paved driveway"></div>
<svg class="abs" style="left:0;top:1900px" width="1200" height="95" viewBox="0 0 1200 95">
  <polygon points="0,0 1200,0 1200,5 0,34" fill="var(--grey-band)"/>
  <polygon points="0,34 1200,5 1200,18 0,90" fill="var(--red)"/>
</svg>
<svg class="abs" style="left:275px;top:2109px" width="50" height="50" viewBox="0 0 50 50">
  <circle cx="25" cy="25" r="24" fill="#fff"/>
  <polygon points="19,14 36,25 19,36" fill="#222"/>
</svg>
<svg class="abs" style="left:652px;top:2014px" width="30" height="24" viewBox="0 0 30 24">
  <path d="M0 12C0 5 4 1 10 0l1 3C7 4 5 7 5 10h6v14H0zM17 12c0-7 4-11 10-12l1 3c-4 1-6 4-6 7h6v14H17z" fill="#333"/>
</svg>
<p class="abs quote-text">Aenean placerat, nibh vel accumsan aliquet, magna nibh accumsan nibh, ac tempus nunc ipsum ac tellus. Cras augue magna, placerat.</p>
<div class="abs quote-name">Mara Linden, City</div>

<!-- contact -->
<h2 class="abs heading contact-title">CONTACT INFO</h2>
<div class="abs contact-line" style="top:2449px">24 Building name, Street name, City Zipcode</div>
<div class="abs contact-line" style="top:2481px;font-weight:700">Phone : 555 019 3307 &nbsp; | &nbsp; Email : hello@plushdwellings.example</div>

<!-- footer -->
<svg class="abs footer" width="1200" height="306" viewBox="0 0 1200 306">
  <polygon points="0,106 1200,0 1200,40" fill="var(--red)"/>
  <polygon points="0,106 1200,40 1200,306 0,306" fill="var(--dark)"/>
</svg>
<div class="abs social"><span></span><span></span><span></span><span></span><span></span></div>
<div class="abs footer-links">Our Properties <span>|</span> Specials <span>|</span> Gallery <span>|</span> Testimonials <span>|</span> About Us <span>|</span> Contact Us <span>|</span> Search Properties</div>
<div class="abs copyright">Copyright &copy; 2018 Plush Dwellings. All rights reserved.</div>

</body>
</html>
```